Menu Design Project for Fastfood Restaurant

I'm looking to redesign my existing menu card for my restaurant.
We make subs, burgers, platters, breakfast and salads among other things.
The theme colors are green, brown and yellow. It should be eye catching with a sleek new age look. The menu should prominently feature the delivery options and numbers, since the concept is highly delivery focused. Also, need to have photographs incorporated into the new menu of selected items (which is currently missing).
Design-wise, wrapzo style visual elements are a good starting point, however, similar designs will not be accepted. The design should be compatible with a4 printing folded into a5 (front and back). However, an a5 front and back is also an acceptable design format.
I have more work for specialized campaigns that i will run, and would like to continue with one designer for all my needs. Please quote "tastora has good subs" in your reply, so i know you've read the above brief.
I'm attaching the existing menu card for an idea of what we have and the items to include
Bring on the creativity.
Reason: I am looking for more submissions. Also changing to a confirmed payment project.
Hi,
This project now has a committed payment, so i hope it's more viable for you all to submit some good designs.
20 to 40 year old professionals, lunch orders
Printing

```html
<!DOCTYPE html>
<html lang="en">
<head>
<meta charset="utf-8">
<title>Tastora Menu</title>
<link rel="stylesheet" href="https://fonts.googleapis.com/css2?family=Anton&family=Oswald:wght@500;700&family=Roboto+Condensed:wght@400;700&family=Signika:wght@400;600&display=swap">
<style>
:root{
  --bg:#e9e4dc;
  --green:#6ba43a;
  --green-dark:#3d7a23;
  --green-deep:#4a8a3a;
  --ochre:#c9952d;
  --brown:#5b2e12;
  --yellow:#e6df2a;
  --yellow-pale:#f1ec7a;
  --orange:#ef9651;
  --salmon:#ef9a7c;
  --red:#e0262b;
  --blue:#1fa3dc;
  --ink:#2b1a0e;
  --white:#ffffff;
}
*{box-sizing:border-box;margin:0;padding:0}
html,body{width:1200px;height:900px;overflow:hidden;background:var(--bg)}
body{font-family:"Roboto Condensed",sans-serif;color:var(--ink);position:relative}
.page{position:absolute;top:180px;width:380px;height:537px;overflow:hidden;box-shadow:0 4px 14px rgba(0,0,0,.18)}
.cover{left:20px;background:var(--green)}
.spread{position:absolute;top:180px;left:420px;width:760px;height:537px;box-shadow:0 4px 14px rgba(0,0,0,.18)}
.spread .page{top:0;box-shadow:none}
.inside-left{left:0;background:var(--orange)}
.inside-right{left:380px;background:var(--yellow)}

/* cover */
.cover-title{position:absolute;left:4px;top:20px;writing-mode:vertical-rl;font-family:"Anton",sans-serif;font-size:86px;line-height:1;color:var(--green-dark);letter-spacing:14px}
.hero-art{position:absolute;left:100px;top:18px;width:268px;height:196px;background:linear-gradient(160deg,#e79a4a 0%,#8fbf4a 100%)}
.brand-name{position:absolute;left:118px;top:100px;font-family:"Oswald",sans-serif;font-weight:700;font-size:44px;color:var(--brown);line-height:1}
.tagline{position:absolute;left:102px;top:226px;font-family:"Signika",sans-serif;font-weight:400;font-size:21px;color:var(--white)}
.contact{position:absolute;left:95px;top:262px;width:285px;height:70px;background:var(--brown);color:var(--white);padding:6px 14px;font-family:"Signika",sans-serif;line-height:1.15}
.contact .addr,.contact .mail{font-size:14px}
.contact .tel{font-size:20px;font-weight:600}
.cover-cols{position:absolute;left:0;top:352px;width:380px;height:185px;display:flex}
.col{width:50%;height:100%;padding:0 8px 0 10px}
.col-bites{background:var(--ochre)}
.col-breakfast{background:var(--green-deep)}
.col-head{font-family:"Oswald",sans-serif;font-weight:700;font-size:21px;margin:0 -8px 6px -10px;padding:2px 10px;background:rgba(255,255,255,.35)}
.col-bites .col-head{color:var(--brown)}
.col-breakfast .col-head{color:var(--white);background:rgba(255,255,255,.2)}
.c-item{display:flex;gap:5px;border-bottom:1px dashed rgba(255,255,255,.45);padding:2px 0 3px;color:var(--white)}
.c-item .p{font-weight:700;font-size:11px;min-width:22px}
.c-item .p small{font-size:6px}
.c-item .n{font-weight:700;font-size:8px;text-transform:uppercase;display:block}
.c-item .d{font-size:7px;font-style:italic;display:block;line-height:1.1}

/* shared menu rows */
.row{display:flex;gap:5px;border-bottom:1px dotted rgba(60,30,10,.45);padding:1px 0 2px}
.row .p{font-weight:700;font-size:10px;min-width:26px}
.row .p small{font-size:6px}
.row .n{font-weight:700;font-size:7.5px;text-transform:uppercase;display:block}
.row .d{font-size:6.5px;display:block;line-height:1.1}
.photo{position:absolute;border:3px solid var(--white);box-shadow:0 1px 3px rgba(0,0,0,.3)}

/* inside left */
.band-top{position:absolute;left:0;top:0;width:380px;height:30px;background:var(--green);font-family:"Anton",sans-serif;color:var(--brown);font-size:22px;padding-left:12px;line-height:30px}
.platters{position:absolute;left:0;top:30px;width:380px;height:168px;background:var(--yellow-pale)}
.platters-title{position:absolute;left:12px;top:4px;font-family:"Anton",sans-serif;font-size:28px;color:var(--brown);line-height:1}
.platters-title span{font-family:"Roboto Condensed",sans-serif;font-size:10px;font-weight:700}
.platters-list{position:absolute;left:12px;top:42px;width:130px}
.lorem{position:absolute;left:150px;top:44px;width:120px;font-weight:700;font-size:10px;line-height:1.15;color:var(--ink)}
.lorem small{display:block;font-weight:400;font-size:6.5px;margin-top:2px}
.salads{position:absolute;left:0;top:198px;width:380px;height:272px;background:var(--orange)}
.salads-head{height:26px;background:#f28a3e;padding-left:12px;font-family:"Anton",sans-serif;font-size:20px;color:var(--white);line-height:26px}
.salads-head em{font-family:"Signika",sans-serif;font-style:normal;font-size:12px;margin-left:6px}
.salads-list{position:absolute;left:12px;top:32px;width:225px}
.drinks{position:absolute;left:0;top:470px;width:380px;height:67px;display:flex}
.drink{width:50%;display:flex;align-items:center;gap:8px;padding:0 10px;color:var(--white)}
.drink-cold{background:var(--blue)}
.drink-hot{background:var(--red)}
.drink h3{font-family:"Signika",sans-serif;font-weight:400;font-size:17px;line-height:1;width:60px}
.drink ul{list-style:none;font-size:8px;line-height:1.2}
.drink b{display:inline-block;width:28px;font-size:8px}

/* inside right */
.super{position:absolute;left:0;top:0;width:380px;height:292px;background:var(--yellow)}
.super-head{position:absolute;left:10px;top:8px;font-family:"Anton",sans-serif;font-size:30px;color:var(--red);line-height:1}
.bites-list{position:absolute;left:10px;top:42px;width:218px;display:flex;flex-direction:column}
.sub-head{font-family:"Anton",sans-serif;font-size:14px;color:var(--brown);line-height:1.1;margin-bottom:1px}
.beef-head{margin-top:5px}
.combo{position:absolute;left:238px;top:118px;width:132px;display:flex;align-items:center;gap:4px;color:var(--red)}
.combo strong{font-family:"Oswald",sans-serif;font-size:14px;display:block;line-height:1}
.combo small{font-size:6px;display:block;font-weight:700}
.combo .price{font-family:"Oswald",sans-serif;font-size:15px;font-weight:700}
.burgers{position:absolute;left:0;top:292px;width:380px;height:210px;background:var(--salmon)}
.burgers-head{position:absolute;left:12px;top:8px;font-family:"Anton",sans-serif;font-size:28px;color:var(--brown);line-height:1}
.burgers-list{position:absolute;left:12px;top:46px;width:215px}
.partners{position:absolute;left:0;top:502px;width:380px;height:35px;background:var(--white);display:flex;align-items:center;gap:12px;padding-left:14px}
.badge{width:24px;height:24px;border-radius:50%}
</style>
</head>
<body>

<section class="page cover">
  <div class="cover-title">MENU</div>
  <div class="hero-art" role="img" aria-label="Illustration of a sub sandwich with cheese, lettuce and sauce"></div>
  <div class="brand-name">Tastora</div>
  <p class="tagline">TASTORA has good subs!</p>
  <div class="contact">
    <div class="addr">one harbor view tower, shop 3</div>
    <div class="mail">order@tastorame.com</div>
    <div class="tel">tel. 04 5550123</div>
  </div>
  <div class="cover-cols">
    <div class="col col-bites">
      <h2 class="col-head">Mornig BITES</h2>
      <div class="c-item"><span class="p">10<small>AED</small></span><span><span class="n">Labneh Wrap</span><span class="d">Labneh, Tomato, Cucumber, Mint, Olives</span></span></div>
      <div class="c-item"><span class="p">18<small>AED</small></span><span><span class="n">Special Halloumi</span><span class="d">Halloumi Cheese, Tomato, Cucumber, Mint, Olives</span></span></div>
      <div class="c-item"><span class="p">15<small>AED</small></span><span><span class="n">Mozzarella Pesto</span><span class="d">Fresh Mozzarella, Tomato, Pesto Sauce</span></span></div>
      <div class="c-item"><span class="p">18<small>AED</small></span><span><span class="n">Greek Feta</span><span class="d">Feta Cheese, Tomato, Cucumber, Mint, Olives</span></span></div>
      <div class="c-item"><span class="p">18<small>AED</small></span><span><span class="n">Cheesy</span><span class="d">Mixed Cheese, Tomato, Cucumber, Olives</span></span></div>
      <div class="c-item"><span class="p">22<small>AED</small></span><span><span class="n">Smoked Turkey</span><span class="d">Turkey Breast, Mozzarella, Tomato, Pickles, Corn, Mustard or Mayo Sauce</span></span></div>
    </div>
    <div class="col col-breakfast">
      <h2 class="col-head">BREAKFAST</h2>
      <div class="c-item"><span class="p">10<small>AED</small></span><span><span class="n">Labneh</span><span class="d">Labneh Plate, Olive Oil, Mint, Mix of Fresh Veggies</span></span></div>
      <div class="c-item"><span class="p">12<small>AED</small></span><span><span class="n">Grilled Halloumi</span><span class="d">2 Pcs, Mix of Fresh Veggies on the side</span></span></div>
      <div class="c-item"><span class="p">15<small>AED</small></span><span><span class="n">Traditional Omlette</span><span class="d">3 Eggs, Mix of Fresh Veggies on the side</span></span></div>
      <div class="c-item"><span class="p">16<small>AED</small></span><span><span class="n">Cheesy Omlette</span><span class="d">3 Eggs with Cheese, Mix of Fresh Veggies on the side</span></span></div>
      <div class="c-item"><span class="p">20<small>AED</small></span><span><span class="n">Tastora Morning</span><span class="d">Labneh, Grilled Halloumi, Thyme &amp; Oil, 2 Eggs, Mix of Vegetables</span></span></div>
    </div>
  </div>
</section>

<div class="spread">
  <section class="page inside-left">
    <div class="band-top">PLATTERS</div>
    <div class="platters">
      <h2 class="platters-title">COMPANY NAME <span>LOREM</span></h2>
      <div class="platters-list">
        <div class="row"><span class="p">25<small>AED</small></span><span><span class="n">Chicken Platter</span><span class="d">Grilled chicken, rice, garlic dip</span></span></div>
        <div class="row"><span class="p">28<small>AED</small></span><span><span class="n">Beef Platter</span><span class="d">Roast beef, fries, side salad</span></span></div>
        <div class="row"><span class="p">22<small>AED</small></span><span><span class="n">Veggie Platter</span><span class="d">Halloumi, grilled veggies, pita</span></span></div>
        <div class="row"><span class="p">30<small>AED</small></span><span><span class="n">Mixed Platter</span><span class="d">Chicken, beef, fries, two sauces</span></span></div>
      </div>
      <p class="lorem">Lorem ipsum dolor sit amet, consectetur adipisicing elit, sed do eiusmod tempor incididunt ut labore et dolore magna aliqua.<small>Ut enim ad minim veniam, quis nostrud exercitation ullamco laboris nisi ut aliquip ex ea commodo consequat.</small></p>
      <div class="photo" role="img" aria-label="Photo of a platter dish" style="left:280px;top:8px;width:90px;height:70px;background:linear-gradient(135deg,#f2d7a8,#c98a4a)"></div>
      <div class="photo" role="img" aria-label="Photo of fried chicken with dip" style="left:280px;top:86px;width:90px;height:70px;background:linear-gradient(135deg,#f0c070,#b8642a)"></div>
    </div>
    <div class="salads">
      <div class="salads-head">SALADS <em>As fresh as it gets</em></div>
      <div class="salads-list">
        <div class="row"><span class="p">18<small>AED</small></span><span><span class="n">Fattoush</span><span class="d">Lettuce, Cucumber, Tomato, Mint, Radish, Toasted Bread</span></span></div>
        <div class="row"><span class="p">18<small>AED</small></span><span><span class="n">Greek Salad</span><span class="d">Lettuce, Tomato, Cucumber, Olives, Feta, Oregano</span></span></div>
        <div class="row"><span class="p">18<small>AED</small></span><span><span class="n">Caesar Salad</span><span class="d">Lettuce, Croutons, Parmesan Cheese and Caesar Sauce</span></span></div>
        <div class="row"><span class="p">18<small>AED</small></span><span><span class="n">Crab Salad</span><span class="d">Crab Sticks, Avocado, Corn, Lettuce, Tartar Sauce</span></span></div>
        <div class="row"><span class="p">18<small>AED</small></span><span><span class="n">Tuna Salad</span><span class="d">Tuna, Lettuce, Corn, Carrots and Lemon Juice</span></span></div>
        <div class="row"><span class="p">18<small>AED</small></span><span><span class="n">Tuna Pasta</span><span class="d">Tuna, Pasta, Corn, Carrots and Lemon Juice</span></span></div>
        <div class="row"><span class="p">18<small>AED</small></span><span><span class="n">Tastora Mix</span><span class="d">Turkey, Lettuce, Fresh Mushrooms, Tomato, Corn</span></span></div>
        <div class="row"><span class="p">18<small>AED</small></span><span><span class="n">Chicken Salad</span><span class="d">Grilled Chicken, Lettuce, Corn, Avocado, Honey Mustard</span></span></div>
        <div class="row"><span class="p">18<small>AED</small></span><span><span class="n">Chicken Pasta</span><span class="d">Grilled Chicken, Pasta, Lettuce, Tomato, Cucumber</span></span></div>
        <div class="row"><span class="p">18<small>AED</small></span><span><span class="n">Chinese Salad</span><span class="d">Grilled Chicken, Lettuce, Mushrooms, Corn, Noodles, Soy</span></span></div>
      </div>
      <div class="photo" role="img" aria-label="Photo of a Greek salad" style="left:250px;top:36px;width:118px;height:68px;background:linear-gradient(135deg,#7fae4a,#d9d2c0)"></div>
      <div class="photo" role="img" aria-label="Photo of a green salad" style="left:250px;top:112px;width:118px;height:68px;background:linear-gradient(135deg,#9cc35a,#e6eccf)"></div>
      <div class="photo" role="img" aria-label="Photo of a tomato and feta salad" style="left:250px;top:188px;width:118px;height:68px;background:linear-gradient(135deg,#c9453a,#8fb85a)"></div>
    </div>
    <div class="drinks">
      <div class="drink drink-cold">
        <h3>COLD DRINKS</h3>
        <ul><li><b>4 AED</b>Soft Drinks</li><li><b>10 AED</b>Fresh Juice</li><li><b>7 AED</b>Ice Tea</li><li><b>3 AED</b>Mineral Water</li><li><b>5 AED</b>Sparkling Water</li></ul>
      </div>
      <div class="drink drink-hot">
        <h3>HOT DRINKS</h3>
        <ul><li><b>10 AED</b>Café Latte</li><li><b>10 AED</b>Espresso</li><li><b>8 AED</b>Cappuccino</li><li><b>8 AED</b>Hot Chocolate</li><li><b>5 AED</b>Kinds of Tea</li></ul>
      </div>
    </div>
  </section>

  <section class="page inside-right">
    <div class="super">
      <h2 class="super-head">SUPER BITES</h2>
      <div class="bites-list">
        <h3 class="sub-head">CHICKEN BITES</h3>
        <div class="row"><span class="p">19<small>AED</small></span><span><span class="n">Breaded Chicken</span><span class="d">Breaded Chicken, Iceberg Lettuce, Corn, Pickles, Cheddar, BBQ Sauce</span></span></div>
        <div class="row"><span class="p">18<small>AED</small></span><span><span class="n">Scaloppini</span><span class="d">Chicken, Coleslaw Salad, Corn, Pickles and Garlic Paste</span></span></div>
        <div class="row"><span class="p">18<small>AED</small></span><span><span class="n">Chicken Tastora</span><span class="d">Grilled Chicken, Mozzarella, Lettuce, Pickles, Light Sauce</span></span></div>
        <div class="row"><span class="p">20<small>AED</small></span><span><span class="n">Fajita</span><span class="d">Chicken, Mixed Pepper, Onion, Corn, Mozzarella, Avocado Sauce</span></span></div>
        <div class="row"><span class="p">17<small>AED</small></span><span><span class="n">Chicken Strips</span><span class="d">Crispy Chicken, Corn, Lettuce, Tomato and Garlic Sauce</span></span></div>
        <div class="row"><span class="p">17<small>AED</small></span><span><span class="n">Chicken Teriyaki</span><span class="d">Chicken, Carrots, Red Cabbage, Mozzarella, Teriyaki Sauce</span></span></div>
        <div class="row"><span class="p">17<small>AED</small></span><span><span class="n">Chicken Tikka</span><span class="d">Chicken, Butter, Onion, Lemon Juice, Mint Coriander Chutney</span></span></div>
        <h3 class="sub-head beef-head">BEEF BITES</h3>
        <div class="row"><span class="p">18<small>AED</small></span><span><span class="n">Roast Bite</span><span class="d">Roast Beef, Mozzarella, Tomato, Lettuce, Pickles, Mayo, Mustard</span></span></div>
        <div class="row"><span class="p">20<small>AED</small></span><span><span class="n">Philly Steak</span><span class="d">Steak, Sautéed Onion, Lettuce, Cheddar Cheese</span></span></div>
        <div class="row"><span class="p">20<small>AED</small></span><span><span class="n">Juicy Steak Bite</span><span class="d">Steak, Onion, Mixed Pepper, BBQ Sauce, Cream and Ketchup</span></span></div>
      </div>
      <div class="photo" role="img" aria-label="Photo of a grilled chicken sub" style="left:240px;top:22px;width:128px;height:80px;background:linear-gradient(135deg,#f4e6c8,#c9924e)"></div>
      <div class="combo">
        <svg width="14" height="30" viewBox="0 0 14 30" aria-hidden="true"><path d="M2 2 L12 15 L2 28" fill="none" stroke="#e0262b" stroke-width="3"/></svg>
        <span><strong>COMBO MEAL</strong><small>ADD FRIES OR GREEN SALAD + SOFT DRINK</small><span class="price">5 AED</span></span>
      </div>
      <div class="photo" role="img" aria-label="Photo of potato wedges with dip" style="left:240px;top:180px;width:128px;height:80px;background:linear-gradient(135deg,#f2c46a,#c87a2a)"></div>
    </div>
    <div class="burgers">
      <h2 class="burgers-head">BURGERS</h2>
      <div class="burgers-list">
        <div class="row"><span class="p">20<small>AED</small></span><span><span class="n">The Original</span><span class="d">Patty, Pickles, Tomato, Lettuce, Cocktail Sauce</span></span></div>
        <div class="row"><span class="p">20<small>AED</small></span><span><span class="n">Cheesy Original</span><span class="d">Patty, Pickles, Tomato, Cheese, Cocktail Sauce</span></span></div>
        <div class="row"><span class="p">25<small>AED</small></span><span><span class="n">Press It</span><span class="d">Patty, Fried Mushrooms, Onion Rings, Swiss Cheese</span></span></div>
        <div class="row"><span class="p">22<small>AED</small></span><span><span class="n">New Yorker</span><span class="d">Patty, Pickles, Tomato, Onion Rings, Swiss Cheese, Mayo</span></span></div>
        <div class="row"><span class="p">18<small>AED</small></span><span><span class="n">Chicken Breast</span><span class="d">Chicken Breast, Tomato, Swiss Cheese, Lettuce, Mayo</span></span></div>
        <div class="row"><span class="p">22<small>AED</small></span><span><span class="n">Supreme Chicken</span><span class="d">Fried Chicken, Cheddar Cheese, Tomato, Lettuce, Pickles</span></span></div>
        <div class="row"><span class="p">20<small>AED</small></span><span><span class="n">Crunchy Chicken</span><span class="d">Crispy Chicken, Lettuce, Tomato, Swiss Cheese, Mayo</span></span></div>
      </div>
      <div class="photo" role="img" aria-label="Photo of a cheeseburger" style="left:238px;top:10px;width:130px;height:58px;background:linear-gradient(135deg,#c9622a,#f0b84a)"></div>
      <div class="photo" role="img" aria-label="Photo of a double burger" style="left:238px;top:76px;width:130px;height:58px;background:linear-gradient(135deg,#8a4a22,#e9c26a)"></div>
      <div class="photo" role="img" aria-label="Photo of a chicken burger with salad" style="left:238px;top:142px;width:130px;height:58px;background:linear-gradient(135deg,#d89a4a,#7aa64a)"></div>
    </div>
    <div class="partners">
      <span class="badge" style="background:#7fb6e0"></span>
      <span class="badge" style="background:#2c5fa8"></span>
      <span class="badge" style="background:#f2c230"></span>
    </div>
  </section>
</div>

</body>
</html>
```